Business Landing Page for SEO Company

Need the landing page of the website designed - I will provide the copy, will need to include details of my company and the services offered, about us, testimonials, faq, etc., and all these elements will need to be arranged graphically on the page.

I want something similar to this: https://pebrovault.com/

Not in terms of color or theme or anything, but we offer a similar service and want to display similar information.

Th services we provide are:

Premium Links
Monthly Links Subscription
Link Insertions

Need to advertise them on the front page. Additionally need a place for testimonials, company details, etc.,

We already have logo for the website. Please use the attached file to insert the logo within the overal design.

Target Market(s)

SEO marketers and agencies

Number of Pages Required

1 page

```html
<!DOCTYPE html>
<html lang="en">
<head>
<meta charset="utf-8">
<title>Linkora — Link Building for SEO Teams</title>
<link rel="stylesheet" href="https://fonts.googleapis.com/css2?family=Poppins:wght@300;400;500;600;700&display=swap">
<style>
:root{
  --blue:#2e8be2;
  --blue-deep:#2a7fd3;
  --blue-soft:#64a3dc;
  --cyan:#22e3df;
  --ink:#2b2b2b;
  --muted:#555;
  --faint:#9a9a9a;
  --white:#fff;
  --placeholder:#e6ebf2;
}
*{margin:0;padding:0;box-sizing:border-box}
html,body{width:1200px;height:3194px;overflow:hidden}
body{font-family:"Poppins",sans-serif;color:var(--ink);background:var(--white);position:relative}
.abs{position:absolute}
.center{left:0;width:1200px;text-align:center}
.btn{position:absolute;display:flex;align-items:center;justify-content:center;width:172px;height:29px;border-radius:2px;font-size:11px;font-weight:500;text-transform:uppercase}
.btn-light{background:var(--white);color:var(--blue)}
.btn-blue{background:var(--blue);color:var(--white)}

/* hero */
.hero{position:absolute;top:0;left:0;width:1200px;height:645px;background:var(--blue);color:var(--white)}
.brand{position:absolute;left:150px;top:14px;font-size:32px;font-weight:500;letter-spacing:-.5px}
.nav{position:absolute;left:370px;top:30px;display:flex;gap:37px;font-size:11px;font-weight:600}
.nav .active{color:var(--cyan)}
.social{position:absolute;display:flex;gap:16px}
.social span{width:29px;height:29px;border-radius:50%;background:var(--white)}
.rule{position:absolute;left:150px;top:74px;width:900px;height:1px;background:rgba(255,255,255,.7)}
.hero-title{top:142px;font-size:36px;font-weight:400}
.hero-title b{color:var(--cyan);font-weight:700}
.hero-sub{top:205px;font-size:12.5px}
.card{position:absolute;top:346px;width:263px;height:225px;border-radius:4px;background:var(--white);color:var(--ink);text-align:center}
.card.featured{background:var(--blue);border:2px solid var(--white);color:var(--white)}
.card .icon{position:absolute;left:74px;top:24px;width:114px;height:104px;border-radius:4px;background:#23234a}
.card.featured .icon{left:72px;top:22px;background:rgba(255,255,255,.85)}
.card h3{position:absolute;top:150px;width:100%;font-size:15px;font-weight:400}
.card.featured h3{top:148px}
.card .btn{left:45px;top:181px}
.card.featured .btn{left:43px;top:179px}

/* testimonials */
.section-title{font-size:24px;font-weight:500}
.section-title em{font-style:normal;color:var(--blue)}
.love-title{top:710px}
.love-rule{left:717px;top:749px;width:76px;height:3px;background:var(--blue)}
.quote{font-family:Georgia,serif;font-weight:700;color:var(--blue);text-align:center}
.testi{position:absolute;text-align:center}
.testi.side{width:200px;font-size:10px;line-height:13px;color:#aaa}
.testi.side .who{margin-top:30px;font-size:11px;line-height:15px;color:#777}
.testi.main{width:250px;font-size:16px;line-height:18px;color:#444}
.testi.main .who{margin-top:30px;font-size:13px;line-height:17px;color:var(--ink);font-weight:500}
.arrow{position:absolute;top:946px}

/* difference */
.diff{position:absolute;top:1241px;left:0;width:1200px;height:557px;background:linear-gradient(100deg,var(--blue-deep),var(--blue-soft));color:var(--white)}
.diff h2{top:66px;font-size:24px;font-weight:400}
.diff h2 b{color:var(--cyan);font-weight:600}
.diff .col{position:absolute;top:165px;width:420px;font-size:13.5px;line-height:27px;font-weight:300}
.diff .col p+p{margin-top:27px}

/* process */
.process-title{top:1862px;font-size:24px;font-weight:400}
.process-title b{color:var(--blue);font-weight:600}
.step{position:absolute;top:1968px;width:300px;text-align:center}
.step .art{width:116px;height:116px;margin:0 auto;border-radius:8px;background:var(--placeholder)}
.step h3{margin-top:30px;font-size:16.5px;font-weight:500}
.step p{margin-top:20px;font-size:13.5px;line-height:27px;color:var(--muted);font-weight:300}

/* search */
.search{position:absolute;top:2413px;left:0;width:1200px;height:284px;background:linear-gradient(180deg,#2e88df,#2478cc);color:var(--white)}
.search h2{top:48px;font-size:24px;font-weight:400}
.search h2 b{color:var(--cyan);font-weight:600}
.search .field{position:absolute;left:315px;top:119px;width:571px;height:48px;border-radius:12px;background:var(--white);color:#888;font-size:12px;padding:16px 22px}
.search .browse{top:210px;font-size:16px;font-weight:600}

/* faq */
.faq-title{left:149px;top:2745px;font-size:20px;font-weight:400}
.faq-col{position:absolute;top:2817px;width:300px}
.faq-col h3{font-size:18.5px;font-weight:500;color:var(--blue)}
.faq-col ul{list-style:none;margin-top:46px}
.faq-col li{font-size:12px;line-height:34.5px;color:#555;font-weight:300}

/* footer */
.footer{position:absolute;top:3096px;left:0;width:1200px;height:98px;background:linear-gradient(100deg,var(--blue-deep),var(--blue-soft));color:var(--white)}
.footer .copy{position:absolute;left:150px;top:42px;font-size:12px}
</style>
</head>
<body>

<header class="hero">
  <div class="brand">Linkora</div>
  <nav class="nav">
    <span class="active">HOME</span><span>SERVICES OFFERED</span><span>TESTIMONIALS</span><span>ABOUT US</span><span>FAQ</span>
  </nav>
  <div class="social" style="left:886px;top:23px"><span></span><span></span><span></span><span></span></div>
  <div class="rule"></div>

  <h1 class="abs center hero-title">WELCOME TO <b>LINKORA</b></h1>
  <p class="abs center hero-sub">Neque porro quisquam est qui dolorem ipsum quia dolor sit amet</p>
  <div class="btn btn-light" style="left:514px;top:253px">Sign up</div>

  <div class="card" style="left:150px">
    <div class="icon" role="img" aria-label="Line icon of a browser window with a search bar and magnifying glass"></div>
    <h3>PREMIUM LINKS</h3>
    <div class="btn btn-blue">Learn more</div>
  </div>
  <div class="card featured" style="left:469px">
    <div class="icon" role="img" aria-label="Line icon of a billboard with content blocks"></div>
    <h3>MONTHLY LINKS</h3>
    <div class="btn btn-light">Subscribe</div>
  </div>
  <div class="card" style="left:787px">
    <div class="icon" role="img" aria-label="Line icon of a browser window with star ratings and a pointing hand"></div>
    <h3>LINK INSERTIONS</h3>
    <div class="btn btn-blue">Learn more</div>
  </div>
</header>

<section>
  <h2 class="abs center section-title love-title">Why customers love <em>Linkora</em></h2>
  <div class="abs love-rule"></div>

  <svg class="arrow" style="left:62px" width="26" height="44" viewBox="0 0 26 44"><path d="M24 2 L3 22 L24 42" fill="none" stroke="#111" stroke-width="2.5"/></svg>
  <svg class="arrow" style="left:1112px" width="26" height="44" viewBox="0 0 26 44"><path d="M2 2 L23 22 L2 42" fill="none" stroke="#111" stroke-width="2.5"/></svg>

  <div class="abs quote" style="left:243px;top:838px;width:100px;font-size:70px;line-height:70px;opacity:.6">&ldquo;</div>
  <div class="testi side" style="left:193px;top:923px">
    Vestibulum tellus ac semper feugiat. Ut sapien lorem, aliquet eget nisl vitae, congue consectetur orci.
    <div class="who">Marek Olsen<br><b>tapfield.co CEO</b></div>
  </div>

  <div class="abs quote" style="left:550px;top:800px;width:100px;font-size:140px;line-height:140px">&ldquo;</div>
  <div class="testi main" style="left:475px;top:923px">
    Vestibulum tellus ac semper feugiat. Ut sapien lorem, aliquet eget nisl vitae, congue consectetur orci.
    <div class="who">Clara-Mae Torvik<br>brightora.org CEO</div>
  </div>

  <div class="abs quote" style="left:857px;top:838px;width:100px;font-size:70px;line-height:70px;opacity:.6">&ldquo;</div>
  <div class="testi side" style="left:807px;top:923px">
    Vestibulum tellus ac semper feugiat. Ut sapien lorem, aliquet eget nisl vitae, congue consectetur orci.
    <div class="who">Tomas Reed<br><b>frostnest.com CEO</b></div>
  </div>

  <div class="btn btn-blue" style="left:514px;top:1138px">More reviews</div>
</section>

<section class="diff">
  <h2 class="abs center">What is different when you work with <b>us?</b></h2>
  <div class="col" style="left:150px">
    <p>Lorem ipsum dolor sit amet, consectetur adipiscing elit. In vestibulum tellus ac semper feugiat. Ut sapien lorem, aliquet eget nisl vitae, congue consectetur orci. Cras accumsan pellentesque mauris ornare ultricies. Nam a commodo velit. Sed venenatis eu dolor a blandit.</p>
    <p>Praesent pellentesque, ex nec dictum laoreet, lorem justo mollis mi, ut efficitur justo arcu quis dolor. Nam ut varius arcu. Integer non felis vitae lacus pretium posuere eu vitae leo. Aliquam dapibus rutrum libero, vulputate iaculis purus eleifend vel. In rhoncus risus nec risus consequat, eget consectetur velit fermentum.</p>
  </div>
  <div class="col" style="left:638px">
    <p>Lorem ipsum dolor sit amet, consectetur adipiscing elit. In vestibulum tellus ac semper feugiat. Ut sapien lorem, aliquet eget nisl vitae, congue consectetur orci. Cras accumsan pellentesque mauris ornare ultricies. Nam a commodo velit. Sed venenatis eu dolor a blandit.</p>
    <p>Praesent pellentesque, ex nec dictum laoreet, lorem justo mollis mi, ut efficitur justo arcu quis dolor. Nam ut varius arcu. Integer non felis vitae lacus pretium.</p>
  </div>
</section>

<section>
  <h2 class="abs center process-title"><b>Our</b> Process</h2>
  <div class="step" style="left:131px">
    <div class="art" role="img" aria-label="Illustration of a computer monitor with a gear and growth chart"></div>
    <h3>Lorem ipsum dolor sit amet</h3>
    <p>Ut sapien lorem, aliquet eget nisl<br>vitae, congue consectetur orci.<br>Cras accumsan pellentesque.</p>
  </div>
  <div class="step" style="left:450px">
    <div class="art" role="img" aria-label="Illustration of a clock inside a gear circled by an arrow"></div>
    <h3>Lorem ipsum dolor sit amet</h3>
    <p>Ut sapien lorem, aliquet eget nisl<br>vitae, congue consectetur orci.<br>Cras accumsan pellentesque.</p>
  </div>
  <div class="step" style="left:768px">
    <div class="art" role="img" aria-label="Illustration of a security shield with a tick inside a gear"></div>
    <h3>Lorem ipsum dolor sit amet</h3>
    <p>Ut sapien lorem, aliquet eget nisl<br>vitae, congue consectetur orci.<br>Cras accumsan pellentesque.</p>
  </div>
  <div class="btn btn-blue" style="left:514px;top:2310px">Sign up now!</div>
</section>

<section class="search">
  <h2 class="abs center">Find Answers to your <b>questions</b></h2>
  <div class="field">Type your question here</div>
  <p class="abs center browse">Or browse below to find your answer</p>
</section>

<section>
  <h2 class="abs faq-title">Frequently Asked Questions</h2>
  <div class="faq-col" style="left:149px">
    <h3>Lorem ipsum</h3>
    <ul><li>Etiam congue risus suscipit</li><li>Etiam congue risus suscipit</li><li>Etiam congue risus</li><li>Etiam congue risus suscipit</li></ul>
  </div>
  <div class="faq-col" style="left:467px">
    <h3>Lorem ipsum</h3>
    <ul><li>Etiam congue risus</li><li>Etiam congue risus suscipit varius quam</li><li>Etiam congue risus suscipit</li><li>Etiam congue risus suscipit</li></ul>
  </div>
  <div class="faq-col" style="left:786px">
    <h3>Lorem ipsum</h3>
    <ul><li>Etiam congue</li><li>Etiam congue risus suscipit</li><li>Etiam congue risus</li><li>Etiamcongue</li></ul>
  </div>
</section>

<footer class="footer">
  <p class="copy">Copyright © 2021 Linkora. All Rights Reserved.</p>
  <div class="social" style="left:886px;top:35px"><span></span><span></span><span></span><span></span></div>
</footer>

</body>
</html>
```